Snowsports equipment company needs a product catalog

Alder is a small snowsports company located in the mountains of Colorado and need a product catalogue for our Telemark Skis and Bindings, also some of the accessories. you can check out our products here: aldercarves.com - we can use the images and copy from the website. We also have a full Brand Standards pdf that is attached. go to aldercarves.com to see products, images, copy.

Products to include: KTV/R, KTV/3, Varno Ski, Pluto Ski, Pivot Kit, RXL Upgrade Kit, 75mm upgrade kit, KTV Brakes, Softer Spring Kit, Mount Glide

We have many hero images to use as well, and you will get access to our google drive folder with images to use.
I am thinking it will be a pdf we send, but may get printed as well.

Target Market(s)

Wholesale accounts, and direct retail customers.

Contact Information for Business Card

simple with use of Brand standards.

Font styles to use
Other font styles liked:
• see brand standards

Requirements
Must have
• Adhere to our brand standards, including colors, fonts, etc.

```html
<!DOCTYPE html>
<html lang="en">
<head>
<meta charset="utf-8">
<title>Alder Catalog — Bindings &amp; Skis</title>
<link rel="stylesheet" href="https://fonts.googleapis.com/css2?family=Barlow:wght@700&display=swap">
<style>
  :root {
    --canvas-bg: #ffffff;
    --page-dark: #0d0d0d;
    --page-mid: #3a3a3a;
    --page-light: #8a8a8a;
    --card-white: #ffffff;
    --card-band: #ececec;
    --frame-line: #e2e2e2;
    --ink: #111111;
    --binding-red: #b3191d;
    --binding-violet: #9a1fc4;
    --binding-steel: #9a9a9a;
    --ski-cool: #6e8fae;
    --ski-warm: #d46a8a;
    --ski-teal: #5fb8a8;
    --ski-amber: #e89a3a;
  }
  * { box-sizing: border-box; margin: 0; padding: 0; }
  html, body {
    width: 1200px; height: 1200px; overflow: hidden;
    background: var(--canvas-bg);
  }
  .catalog-page {
    position: absolute;
    left: 175px; top: 50px;
    width: 851px; height: 1101px;
    overflow: hidden;
  }
  .page-backdrop {
    position: absolute; inset: 0;
    background:
      radial-gradient(ellipse 60% 30% at 30% 15%, rgba(138,138,138,.35), transparent 70%),
      radial-gradient(ellipse 40% 60% at 85% 70%, rgba(138,138,138,.3), transparent 70%),
      radial-gradient(ellipse 50% 25% at 40% 95%, rgba(200,200,200,.3), transparent 70%),
      linear-gradient(160deg, var(--page-dark) 0%, var(--page-mid) 45%, var(--page-dark) 100%);
  }
  .product-card {
    position: absolute;
    width: 310px; height: 426px;
    background: var(--card-white);
  }
  .product-card.col-left { left: 78px; }
  .product-card.col-right { left: 462px; }
  .product-card.row-top { top: 94px; }
  .product-card.row-bottom { top: 586px; }
  .product-visual {
    position: absolute;
    left: 13px; top: 8px; width: 284px; height: 272px;
    border: 1px solid var(--frame-line);
  }
  .product-shot {
    position: absolute;
    border-radius: 6px;
  }
  .shot-binding {
    left: 50px; top: 70px; width: 200px; height: 44px;
    transform: rotate(-38deg);
    transform-origin: center;
    top: 110px; left: 38px;
  }
  .shot-binding.red { background: linear-gradient(90deg, var(--binding-red), var(--binding-steel) 30%, #444 60%, var(--binding-red) 80%, var(--binding-steel)); }
  .shot-binding.violet { background: linear-gradient(90deg, var(--binding-steel), #444 40%, var(--binding-violet) 60%, var(--binding-steel) 80%, var(--binding-violet)); }
  .shot-ski {
    top: 46px; left: 122px; width: 40px; height: 212px;
    border-radius: 10px 10px 4px 4px;
  }
  .shot-ski.varno { background: linear-gradient(180deg, #444 0%, var(--ski-cool) 30%, var(--ski-warm) 45%, #888 70%, #552a2a 100%); }
  .shot-ski.pluto { background: linear-gradient(180deg, var(--ski-teal) 0%, #9ad0c8 35%, var(--ski-warm) 65%, var(--ski-amber) 100%); }
  .product-label {
    position: absolute;
    left: 0; right: 0; bottom: 0; height: 138px;
    background: var(--card-band);
    display: flex; align-items: center; justify-content: center;
    padding-bottom: 12px;
    font-family: "Barlow", sans-serif;
    font-weight: 700;
    font-size: 38px;
    letter-spacing: 0.5px;
    text-transform: uppercase;
    color: var(--ink);
  }
</style>
</head>
<body>
  <main class="catalog-page">
    <div class="page-backdrop" role="img" aria-label="Dark flowing smoke-like swirl texture in black and grey"></div>

    <article class="product-card col-left row-top">
      <div class="product-visual">
        <div class="product-shot shot-binding red" role="img" aria-label="KTV/R telemark binding with red toe and heel parts"></div>
      </div>
      <h2 class="product-label">KTV/R</h2>
    </article>

    <article class="product-card col-right row-top">
      <div class="product-visual">
        <div class="product-shot shot-binding violet" role="img" aria-label="KTV/3 telemark binding with purple toe and heel parts"></div>
      </div>
      <h2 class="product-label">KTV/3</h2>
    </article>

    <article class="product-card col-left row-bottom">
      <div class="product-visual">
        <div class="product-shot shot-ski varno" role="img" aria-label="Pair of Varno skis with mountain and forest topsheet artwork"></div>
      </div>
      <h2 class="product-label">Varno Ski</h2>
    </article>

    <article class="product-card col-right row-bottom">
      <div class="product-visual">
        <div class="product-shot shot-ski pluto" role="img" aria-label="Pair of Pluto skis with colorful teal, pink and amber marbled topsheet"></div>
      </div>
      <h2 class="product-label">Pluto Ski</h2>
    </article>
  </main>
</body>
</html>
```